Business Card for Restaurant Nuvelo

This project consist of creating 2 design for business card of restaurant named Nuvelo.

The attached specs below are 'ONLY SUGGESTION' if you have others ideas. You are welcome to post it.

1) Restaurant Card

Adresse:
2318 Rue des Pruniers
Montréal (Qc) H3K 2T8

Website:
www.nu-velo.ca

Phone:
438-552-0194

2) Employee Card

Name: Greta Lund
Title: Owner

Address:
2318 Rue des Pruniers
Montréal (Qc) H3K 2T8

Email:greta@nu-velo.ca
Phone Number:438-552-0194
Cellphone Number:514-730-4816

 The attached specs are 'ONLY SUGGESTION' if you have others ideas.  You are welcome to post it.

Industry/Entity Type

Restaurant

Requirements
Must have
• UV Card Spot

To print Spot UV business cards you would have to submit 2 files for each side. The first file "base" would be your regular design file as it would have been in any other case. The 2nd file "UV mask" is a black/white file. The BLACK color will indicate the areas that will be covered with the UV high gloss finish. To upload the files, please combine front design and front mask file in one P
Nice to have
• 1) The font of the logo should be ink effect
2) black background with wallpaper effect
3) The specs below are 'ONLY SUGGESTION' if you have others ideas. You are welcome to post it.

```html
<!DOCTYPE html>
<html lang="en">
<head>
<meta charset="utf-8">
<title>Restaurant Nuvelo – Business Cards</title>
<link rel="stylesheet" href="https://fonts.googleapis.com/css2?family=Montserrat:wght@400;500;600;700&family=Roboto+Condensed:wght@400;700&family=Noto+Sans+JP:wght@500&display=swap">
<style>
  :root {
    --stage-red: #c8202c;
    --stage-red-dark: #a5161f;
    --card-black: #1b1b1b;
    --card-black-light: #2e2e2e;
    --card-white: #ffffff;
    --ink-white: #f4f4f4;
    --accent-red: #e02a1c;
    --lantern-red: #e8402a;
    --lantern-dark: #b5180f;
    --text-dark: #1a1a1a;
    --text-grey: #8a8a8a;
    --label-white: #ffffff;
    --label-rose: #c9665f;
    --mask-grey: #7a7a7a;
  }
  * { box-sizing: border-box; margin: 0; padding: 0; }
  html, body { width: 1200px; height: 900px; overflow: hidden; }
  body {
    position: relative;
    background: radial-gradient(ellipse at 60% 40%, var(--stage-red) 0%, var(--stage-red-dark) 100%);
    font-family: "Montserrat", Arial, sans-serif;
  }

  /* presentation labels */
  .label {
    position: absolute;
    font-family: "Roboto Condensed", Arial, sans-serif;
    font-size: 20px;
    padding: 5px 14px;
    line-height: 1.15;
  }
  .label--white { background: var(--label-white); color: var(--text-dark); }
  .label--rose { background: var(--label-rose); color: var(--label-white); }
  .label small { display: block; font-size: 15px; text-align: center; }

  /* cards */
  .card {
    position: absolute;
    width: 500px;
    height: 286px;
    overflow: hidden;
    box-shadow: 0 14px 28px rgba(0,0,0,.35);
  }
  .card--dark {
    background:
      repeating-linear-gradient(0deg, rgba(255,255,255,.025) 0 1px, transparent 1px 3px),
      linear-gradient(160deg, var(--card-black-light) 0%, var(--card-black) 60%, #0f0f0f 100%);
    color: var(--ink-white);
  }
  .card--light { background: var(--card-white); color: var(--text-dark); }

  .lantern-shadow {
    position: absolute;
    border-radius: 46% 46% 40% 40%;
    background: linear-gradient(180deg, #3c3c3c 0%, #262626 100%);
  }
  .lantern-red {
    position: absolute;
    border-radius: 46%;
    background: radial-gradient(circle at 40% 40%, var(--lantern-red) 0%, var(--lantern-dark) 100%);
  }

  .brand {
    position: absolute;
    display: flex;
    align-items: center;
    gap: 10px;
  }
  .brand__name {
    font-family: "Montserrat", Arial, sans-serif;
    font-weight: 700;
    color: var(--ink-white);
    letter-spacing: 1px;
    line-height: 1;
  }
  .brand__dot {
    border-radius: 50%;
    background: var(--accent-red);
  }
  .tagline {
    position: absolute;
    font-size: 13px;
    font-weight: 500;
    color: var(--ink-white);
    white-space: nowrap;
  }
  .tagline .sep { color: var(--accent-red); padding: 0 4px; }
  .tagline .jp { font-family: "Noto Sans JP", sans-serif; }

  .address, .contact-line {
    position: absolute;
    font-size: 12px;
    font-weight: 600;
    line-height: 1.35;
  }

  /* employee back */
  .person__name { position: absolute; left: 34px; top: 28px; font-size: 26px; font-weight: 500; }
  .person__title { position: absolute; left: 36px; top: 62px; font-size: 13px; color: var(--text-grey); }
  .person__details { position: absolute; left: 36px; top: 100px; font-size: 14px; line-height: 1.4; }
  .person__details .caption { font-size: 12px; font-weight: 600; }
  .person__details .row { display: flex; align-items: center; gap: 7px; }
  .person__details svg { width: 14px; height: 14px; flex: none; }
  .back-panel {
    position: absolute;
    right: 28px; top: 22px;
    width: 150px; height: 242px;
    background: var(--card-black);
    outline: 3px solid #6b6b6b;
    outline-offset: 4px;
  }

  /* UV masks */
  .mask {
    position: absolute;
    width: 170px; height: 286px;
    background: var(--card-white);
    box-shadow: 0 8px 16px rgba(0,0,0,.3);
  }
  .mask__title {
    background: var(--mask-grey);
    color: var(--label-white);
    font-family: "Roboto Condensed", Arial, sans-serif;
    font-size: 12px;
    padding: 3px 8px;
  }
  .mask__fill { position: absolute; background: #000; }
  .mask__frame {
    position: absolute;
    left: 16px; right: 16px; top: 34px; bottom: 16px;
    border: 4px solid #000;
  }
</style>
</head>
<body>

  <!-- Employee card, front -->
  <div class="label label--white" style="left:60px; top:30px;">Employee card</div>
  <div class="label label--rose" style="left:60px; top:72px;">Front</div>
  <section class="card card--dark employee-front" style="left:60px; top:115px;">
    <div class="lantern-shadow" role="img" aria-label="Large dark paper lantern illustration" style="left:-40px; top:30px; width:220px; height:240px;"></div>
    <div class="brand" style="left:110px; top:78px;">
      <span class="brand__name" style="font-size:76px;">Nuvelo</span>
      <span class="brand__dot" style="width:18px; height:18px;"></span>
    </div>
    <p class="tagline" style="left:116px; top:170px;">Resto-Bar Japonais<span class="sep">·</span>Izakaya<span class="sep">·</span><span class="jp">居酒屋</span></p>
    <div class="lantern-red" role="img" aria-label="Red paper lantern illustration with vertical Japanese lettering" style="left:410px; top:160px; width:70px; height:110px; border-radius:30px;"></div>
  </section>

  <!-- Restaurant card, front -->
  <div class="label label--white" style="left:640px; top:30px; text-align:center;">Restaurant card<small>(front side only)</small></div>
  <section class="card card--dark restaurant-front" style="left:640px; top:115px;">
    <div class="brand" style="left:130px; top:40px;">
      <span class="brand__name" style="font-size:70px;">Nuvelo</span>
      <span class="brand__dot" style="width:16px; height:16px;"></span>
    </div>
    <p class="tagline" style="left:136px; top:126px;">Resto-Bar Japonais<span class="sep">·</span>Izakaya<span class="sep">·</span><span class="jp">居酒屋</span></p>
    <p class="address" style="left:30px; top:170px;">2318 Rue des Pruniers<br>Montréal (Qc) H3K 2T8</p>
    <div class="lantern-red" role="img" aria-label="Red paper lantern illustration with vertical Japanese lettering" style="left:400px; top:130px; width:64px; height:90px; border-radius:28px;"></div>
    <p class="contact-line" style="right:26px; top:232px; text-align:right;">Ph: 438-552-0194<br>www.nu-velo.ca</p>
  </section>

  <!-- Employee card, back -->
  <div class="label label--rose" style="left:60px; top:455px;">back</div>
  <section class="card card--light employee-back" style="left:60px; top:500px;">
    <h1 class="person__name">Greta Lund</h1>
    <p class="person__title">Owner</p>
    <div class="person__details">
      <p class="caption">Address:</p>
      <p>2318 Rue des Pruniers<br>Montréal (Qc) H3K 2T8</p>
      <p class="row">
        <svg viewBox="0 0 16 16"><rect x="1" y="3" width="14" height="10" fill="none" stroke="#1a1a1a" stroke-width="1.6"/><path d="M1 3l7 6 7-6" fill="none" stroke="#1a1a1a" stroke-width="1.6"/></svg>
        greta@nu-velo.ca
      </p>
      <p class="row">
        <svg viewBox="0 0 16 16"><path d="M4 1h3l1 4-2 1.5c.8 2 2 3.2 3.5 3.5L11 8l4 1v3c0 1.5-1 2-2 2C7 14 2 9 2 3c0-1 .5-2 2-2z" fill="#1a1a1a"/></svg>
        438-552-0194
      </p>
      <p class="row">
        <svg viewBox="0 0 16 16"><rect x="4" y="1" width="8" height="14" rx="1.5" fill="#1a1a1a"/><rect x="5.5" y="3" width="5" height="8" fill="#fff"/></svg>
        514-730-4816
      </p>
    </div>
    <div class="back-panel">
      <div class="lantern-red" role="img" aria-label="Red paper lantern illustration with vertical Japanese lettering" style="left:35px; top:110px; width:80px; height:110px; border-radius:34px;"></div>
    </div>
  </section>

  <!-- UV masks -->
  <aside class="mask mask--front" style="left:780px; top:520px;">
    <p class="mask__title">UV MASK (front)</p>
    <div class="mask__fill" role="img" aria-label="Black spot UV area covering the large lantern shape" style="left:0; top:60px; width:120px; height:200px; border-radius:0 50% 40% 0;"></div>
  </aside>
  <aside class="mask mask--back" style="left:970px; top:520px;">
    <p class="mask__title">UV MASK (back)</p>
    <div class="mask__frame"></div>
    <div class="mask__fill" role="img" aria-label="Black spot UV area covering the small lantern shape" style="left:60px; top:180px; width:50px; height:56px; border-radius:45%;"></div>
  </aside>

</body>
</html>
```